Paws Haven

Need Yard signs
Dimensions 24" wide and 18" high

Copy: Rescue does not mean "Damaged". It means they have been let down by humans.
Please adopt at: 782 W Marlowe Ave, Tampa, Fl 33647
Open: Tues-Sun 10am - 7pm

I have attached a sample of the original ad. I can't use this because the resolution is too low and the type has to be big enough so that it can be seen 12 feet away.
I have also attached some photos you can use. The res may not be hi enough, but perhaps you can find some stock photography even these pics are not hi res enough.

Target Market(s)

animal lovers

Font styles to use
Sans Serif

Colors

Designer to choose colors to be used in the design.

Requirements
Must have
• Must be easy to read.

```html
<!DOCTYPE html>
<html lang="en">
<head>
<meta charset="utf-8">
<title>Paws Haven – Yard Sign</title>
<link href="https://fonts.googleapis.com/css2?family=Montserrat:wght@800&family=Raleway:wght@300&family=Hind:wght@600&display=swap" rel="stylesheet">
<style>
  :root {
    --page: #f2f2f2;
    --sign: #ffffff;
    --navy: #0b0f6b;
    --green: #86c232;
    --ink: #3a3a3a;
    --photo-tan: #b98a55;
    --photo-teal: #8ea6ac;
    --photo-cream: #e8dccb;
  }
  * { margin: 0; padding: 0; box-sizing: border-box; }
  html, body { width: 1200px; height: 899px; overflow: hidden; background: var(--page); }
  .sign {
    position: absolute; left: 295px; top: 19px;
    width: 610px; height: 860px;
    background: var(--sign);
  }
  .brand {
    position: absolute; left: 37px; top: 33px;
    width: 117px; height: 40px;
    border: 1px solid var(--navy);
    display: flex; align-items: center; justify-content: center;
    font-family: "Hind", sans-serif; font-weight: 600; font-size: 15px;
    color: var(--navy);
  }
  .hero-photo { position: absolute; left: 49px; top: 16px; width: 518px; height: 497px; }
  .message {
    position: absolute; left: 64px; top: 540px;
    width: 485px; height: 166px;
    border: 1px solid var(--navy);
    text-align: center; color: var(--ink);
  }
  .message .lead {
    position: absolute; left: 50%; top: -13px; transform: translateX(-50%);
    background: var(--sign); padding: 0 4px; white-space: nowrap;
    font-family: "Raleway", sans-serif; font-weight: 300; font-size: 23px; letter-spacing: 0.5px;
  }
  .message .headline {
    margin-top: 18px;
    font-family: "Montserrat", sans-serif; font-weight: 800; font-size: 80px; line-height: 1;
    color: var(--green); letter-spacing: -1px;
  }
  .message .sub {
    margin-top: 8px;
    font-family: "Raleway", sans-serif; font-weight: 300; font-size: 23px; line-height: 27px;
  }
  .info-band {
    position: absolute; left: 19px; top: 732px;
    width: 573px; height: 107px;
    background: var(--navy); color: #fff;
    display: flex; flex-direction: column; align-items: center; justify-content: center; gap: 2px;
    font-family: "Hind", sans-serif; font-weight: 600; font-size: 29px;
  }
  .info-band .row { display: flex; align-items: center; gap: 10px; }
  .info-band svg { flex: none; }
</style>
</head>
<body>
  <main class="sign">
    <div class="brand">Paws Haven</div>

    <svg class="hero-photo" viewBox="0 0 518 497" role="img" aria-label="Photo of a tan and white rescue dog sitting in a shelter kennel">
      <defs>
        <linearGradient id="photoTone" x1="0" y1="0" x2="1" y2="1">
          <stop offset="0" stop-color="var(--photo-teal)"/>
          <stop offset="0.5" stop-color="var(--photo-tan)"/>
          <stop offset="1" stop-color="var(--photo-cream)"/>
        </linearGradient>
      </defs>
      <path fill="url(#photoTone)" d="M150 0 L390 0 L410 40 L450 50 L470 110 L500 150 L505 230 L490 290 L510 340 L500 420 L480 470 L455 497 L440 470 L400 480 L330 470 L260 480 L180 475 L110 460 L70 440 L40 380 L55 320 L20 270 L0 200 L25 160 L40 110 L80 90 L110 50 Z"/>
    </svg>

    <section class="message">
      <p class="lead">RESCUE DOES NOT MEAN</p>
      <h1 class="headline">DAMAGED</h1>
      <p class="sub">IT MEANS THEY HAVE BEEN LET DOWN<br>BY HUMANS</p>
    </section>

    <footer class="info-band">
      <div class="row">
        <svg width="24" height="24" viewBox="0 0 24 24" aria-hidden="true">
          <rect x="2" y="4" width="17" height="16" rx="2" fill="none" stroke="var(--green)" stroke-width="2"/>
          <line x1="2" y1="9" x2="19" y2="9" stroke="var(--green)" stroke-width="2"/>
          <circle cx="18" cy="18" r="5" fill="var(--navy)" stroke="var(--green)" stroke-width="2"/>
          <path d="M18 15.5 V18 H20" fill="none" stroke="var(--green)" stroke-width="1.5"/>
        </svg>
        <span>Tues-Sun 10am - 7pm</span>
      </div>
      <div class="row">
        <svg width="18" height="24" viewBox="0 0 18 24" aria-hidden="true">
          <path d="M9 1 C4.5 1 1 4.5 1 9 C1 15 9 23 9 23 C9 23 17 15 17 9 C17 4.5 13.5 1 9 1 Z" fill="var(--green)"/>
          <circle cx="9" cy="9" r="3" fill="var(--navy)"/>
        </svg>
        <span>782 W Marlowe Ave, Tampa, Fl 33647</span>
      </div>
    </footer>
  </main>
</body>
</html>
```